TVF web design

We need a homepage web design concept for a new company based in Brisbane called 'Tarvel Fabrication'. They design, manufacture and repair of all forms of operator Roll Over Protective Structures or ROPS, and Falling Object Protective Structures or FOPS canopies and cabins.
Updates
Sorry link to website is incorrect should be http://www.norbeckfab.com.au/
Thanks
Hi Everyone
I am presenting designs to my client on Wednesday so will let you feedback.
Cheers
Mags
Target Market(s)
Adults in construction industry and their Agents/Distributors
Industry/Entity Type
Construction
Number of Pages Required
1 page
Requirements
Must have
- Main Navigation
- o Home
- o About Us
- - Mission and Values
- - Facilities
- - Terms and Conditions
- - Jobs
- o Rops/Fops
- o Cabins
- o Crane Repairs
- o Other Products
- o Links
- o Contact Us
- - Client wants a sleek, corporate look and feel an example of a site they like is www.corvinlode.com.au
- - Client is rebranding and I have attached some sample new brochures that contains their new corporate colours etc as a guideline for the direction they are going.
- - The following elements are to be included in the design concept:
- o Homepage
- - Room for a Flash banner of rotating images in banner
- - Phone number should appear on every page 07 4819 6307
- - Horizontal navigation (can you show how drop down will appear as well)
- - Logo is attached (bear in mind this will be changing to new corporate colours) so just use the one attached but colours need to be in line with their new colours.
- - Tagline is “It’s the choice you make, not the change you take that determines your safety!” this needs to be displayed on every page of the site.
- - New Corporate colours are orange: RGB - 239 - 179 - 47 (colour 1) to RGB 239 - 121 - 47 (colour 2) and grey: RGB - 46 - 54 – 64
- - Intro text on page somewhere
- - 3 containers/icons to highlight areas on site – Rops/Fops, Sign up to our enewsletter and Contact Us
- - Images – have attached a few that can be used in concepts.

```html
<!DOCTYPE html>
<html lang="en">
<head>
<meta charset="utf-8">
<title>Tarvel Fabrication — Superior ROPS Cabin Standards</title>
<link rel="stylesheet" href="https://fonts.googleapis.com/css2?family=Barlow:wght@500;600&family=Barlow+Semi+Condensed:wght@500;600&display=swap">
<style>
  :root {
    --orange-1: #efb32f;
    --orange-2: #ef792f;
    --grey: #2e3640;
    --grey-deep: #232a33;
    --page-bg: #25282c;
    --text-light: #ffffff;
    --text-muted: #b9bcc0;
    --accent-red: #e8352a;
    --line-dark: #0d0f12;
  }
  * { box-sizing: border-box; margin: 0; padding: 0; }
  html, body { width: 1200px; height: 983px; overflow: hidden; }
  body {
    background: radial-gradient(ellipse at 50% 40%, #34383d 0%, var(--page-bg) 60%, #1b1d20 100%);
    font-family: Arial, Helvetica, sans-serif;
    position: relative;
  }
  .frame {
    position: absolute;
    background: linear-gradient(180deg, var(--orange-1), var(--orange-2));
  }
  .frame-inner {
    position: absolute;
    background: linear-gradient(180deg, var(--grey-deep), var(--grey));
  }

  /* Header */
  .site-header { left: 109px; top: 0; width: 982px; height: 218px; }
  .site-header .frame-inner { left: 11px; top: 0; right: 11px; bottom: 11px; background: linear-gradient(180deg, #0c0e10, var(--grey)); }
  .brand {
    position: absolute; left: 26px; top: 66px; width: 180px;
    display: flex; align-items: center; gap: 10px;
  }
  .brand-mark { width: 18px; height: 18px; border-radius: 50%; background: var(--orange-1); flex: none; }
  .brand-name {
    font-family: "Barlow", sans-serif; font-weight: 600; font-size: 24px; line-height: 1.05;
    color: var(--orange-1);
  }
  .brand-strap {
    position: absolute; left: 15px; top: 180px;
    font-family: Arial, sans-serif; font-weight: bold; font-size: 14px; color: var(--accent-red);
  }
  .banner {
    position: absolute; left: 236px; top: 22px; width: 702px; height: 142px;
    border: 2px solid #e9e9e9; display: flex; background: #fff;
  }
  .banner-slide { flex: 1; }
  .slide-truck { background: linear-gradient(135deg, #e9a824, #c77d12); }
  .slide-frame { background: linear-gradient(135deg, #b4b4b4, #6d6d75); }
  .slide-cab { background: linear-gradient(135deg, #f2f2f2, #a9acb0); }
  .tagline {
    position: absolute; left: 251px; top: 175px;
    font-family: "Barlow", sans-serif; font-weight: 500; font-size: 20px; color: var(--text-muted);
  }

  /* Navigation */
  .main-nav { left: 109px; top: 229px; width: 982px; height: 44px; display: flex; }
  .main-nav a {
    display: flex; align-items: center; justify-content: center;
    height: 100%; border-right: 2px solid #c4611f; border-left: 1px solid #f6cc6a;
    font-family: "Barlow Semi Condensed", sans-serif; font-weight: 500; font-size: 20px;
    color: var(--grey); text-decoration: none; letter-spacing: 0.3px;
  }
  .main-nav a:last-child { border-right: none; }

  /* Sidebar */
  .sidebar { left: 109px; top: 284px; width: 311px; height: 545px; }
  .sidebar .frame-inner { left: 11px; top: 11px; right: 11px; bottom: 11px; padding: 19px 16px; }
  .sidebar h2 {
    font-family: "Barlow", sans-serif; font-weight: 600; font-size: 19px; color: var(--orange-1);
    margin-bottom: 2px;
  }
  .sidebar h2 .news-date { font-family: Arial, sans-serif; font-weight: normal; font-size: 13px; color: var(--text-light); margin-left: 6px; }
  .sidebar p { font-size: 13.5px; line-height: 17.5px; color: var(--text-light); margin-bottom: 17px; }
  .sidebar hr { border: none; border-top: 3px solid var(--line-dark); margin: 12px 0 14px; }

  /* Main content */
  .content { left: 431px; top: 284px; width: 660px; height: 545px; }
  .content .frame-inner { left: 11px; top: 11px; right: 11px; bottom: 11px; }
  .content h1 {
    position: absolute; left: 20px; top: 12px;
    font-family: "Barlow", sans-serif; font-weight: 600; font-size: 40px; color: var(--text-light);
  }
  .feature {
    position: absolute; left: 22px; top: 68px; width: 594px; height: 338px;
    border: 1px solid #8a8f96;
  }
  .feature-media {
    height: 305px;
    background: linear-gradient(180deg, #4f7aa6 0%, #8a6a35 35%, #d6a24a 60%, #9b6b2c 100%);
    position: relative;
  }
  .play-label {
    position: absolute; right: 20px; top: 14px;
    font-family: "Barlow Semi Condensed", sans-serif; font-size: 12px; color: #e6e6e6;
  }
  .feature-tabs { display: flex; height: 32px; background: #2b2b28; }
  .feature-tabs span {
    flex: 1; display: flex; align-items: center; justify-content: center;
    border-right: 1px solid #8a8f96;
    font-family: "Barlow Semi Condensed", sans-serif; font-weight: 600; font-size: 12px; color: #b3b3b3;
  }
  .feature-tabs span:last-child { border-right: none; }
  .intro {
    position: absolute; left: 22px; top: 424px; width: 598px;
    font-size: 13px; line-height: 15.5px; color: var(--orange-1);
  }

  /* Footer bar */
  .action-bar { left: 109px; top: 840px; width: 982px; height: 47px; }
  .action {
    position: absolute; top: 8px; height: 32px; background: var(--grey);
    display: flex; align-items: center; gap: 10px; padding-left: 8px;
    font-family: "Barlow Semi Condensed", sans-serif; font-weight: 600; font-size: 13.5px;
    color: var(--orange-1); text-decoration: none; letter-spacing: 0.3px;
  }
  .action svg { flex: none; }
  .action-rops { left: 8px; width: 132px; }
  .action-contact { left: 147px; width: 131px; }
  .action-newsletter { left: 286px; width: 210px; }
  .phone {
    position: absolute; right: 10px; top: 3px;
    font-family: "Barlow Semi Condensed", sans-serif; font-weight: 600; color: var(--grey);
    display: flex; align-items: baseline; gap: 8px;
  }
  .phone small { font-size: 19px; font-weight: 500; }
  .phone strong { font-size: 34px; font-weight: 600; }
  .copyright {
    position: absolute; right: 106px; top: 903px;
    font-size: 13.5px; color: var(--orange-1); letter-spacing: 0.5px;
  }
</style>
</head>
<body>

<header class="frame site-header">
  <div class="frame-inner">
    <div class="brand">
      <span class="brand-mark"></span>
      <span class="brand-name">Tarvel Fabrication</span>
    </div>
    <div class="brand-strap">High Performance Workplace</div>
    <div class="banner">
      <div class="banner-slide slide-truck" role="img" aria-label="Orange truck cab door bearing company name"></div>
      <div class="banner-slide slide-frame" role="img" aria-label="Fabricated steel roll over protective frame"></div>
      <div class="banner-slide slide-cab" role="img" aria-label="White truck cab with fitted protective structure"></div>
    </div>
    <p class="tagline">It’s the choice you make, not the change you take that determines your safety!”</p>
  </div>
</header>

<nav class="frame main-nav">
  <a href="#" style="width:84px">HOME</a>
  <a href="#" style="width:110px">ABOUT US</a>
  <a href="#" style="width:133px">ROPS / FOPS</a>
  <a href="#" style="width:89px">CABINS</a>
  <a href="#" style="width:164px">CRANE REPAIRS</a>
  <a href="#" style="width:181px">OTHER PRODUCTS</a>
  <a href="#" style="width:76px">LINKS</a>
  <a href="#" style="width:145px">CONTACT US</a>
</nav>

<aside class="frame sidebar">
  <div class="frame-inner">
    <h2>Welcome to Tarvel Fabrication!</h2>
    <p>Lorem ipsum dolor sit amet, consectetur adipiscing elit. Cras egestas, turpis ac elementum porta, justo mauris vulputate enim, nec volutpat nulla nunc non velit.</p>
    <p>Fusce tellus dui, volutpat at varius vulputate, sodales sit amet ante.</p>
    <p>Integer tempor lectus nec nibh sollicitud congue. Vivamus fermentum egestas .</p>
    <hr>
    <h2>The Latest News <span class="news-date">&gt; 06.18.09</span></h2>
    <p>Lorem ipsum dolor sit amet, consectetur adipiscing elit. Cras egestas, turpis ac elementum porta, justo mauris vulputate enim, nec volutpat nulla nunc non velit.</p>
    <p>Fusce tellus dui, volutpat at varius vulputate, sodales sit amet ante.</p>
    <p>Integer tempor lectus nec nibh sollicitud congue. Vivamus fermentum egestas .</p>
  </div>
</aside>

<main class="frame content">
  <div class="frame-inner">
    <h1>Superior ROPS Cabin Standards</h1>
    <div class="feature">
      <div class="feature-media" role="img" aria-label="Yellow dump truck on a dirt work site">
        <span class="play-label">▶ PLAY</span>
      </div>
      <div class="feature-tabs">
        <span>CABIN</span><span>CRANE</span><span>ROPS</span><span>FOPS</span>
        <span>REPAIRS</span><span>PARTS</span><span>FAB</span><span>EXCAVATOR</span>
      </div>
    </div>
    <p class="intro">Lorem ipsum dolor sit amet, consectetur adipiscing elit. Cras egestas, turpis ac elementum porta, justo mauris vulputate enim, nec volutpat nulla nunc non velit. Fusce tellus dui, volutpat at varius vulputate, sodales sit amet ante. Integer tempor lectus nec nibh sollicitudin congue. Vivamus fermentum egestas dignissim. Donec non massa felis. Aliquam id lectus vel nisl tempus auctor.</p>
  </div>
</main>

<footer class="frame action-bar">
  <a href="#" class="action action-rops">
    <svg width="28" height="18" viewBox="0 0 28 18"><path d="M1 17V9h5V4h3v5h4V1h3v8h11v8z" fill="#fff"/></svg>
    ROPS / FOPS
  </a>
  <a href="#" class="action action-contact">
    <svg width="32" height="18" viewBox="0 0 32 18"><path d="M8 1h23v16H8z" fill="#fff"/><path d="M8 1l11.5 9L31 1" fill="none" stroke="#2e3640" stroke-width="2"/><path d="M0 7h6M2 11h5" stroke="#fff" stroke-width="2"/></svg>
    CONTACT US
  </a>
  <a href="#" class="action action-newsletter">
    <svg width="20" height="20" viewBox="0 0 20 20"><path d="M4 1h15l-3 18H1z" fill="#fff"/><path d="M6 6h9M5.5 9h9M5 12h9M4.5 15h7" stroke="#2e3640" stroke-width="1.5"/></svg>
    SIGN UP FOR NEWSLETTER
  </a>
  <div class="phone"><small>Call us anytime</small><strong>07 4819 6307</strong></div>
</footer>

<p class="copyright">© 2009 Tarvel Fabrication Inc.</p>

</body>
</html>
```